Need web redesign for cybersecurity startup whose mission is to make robust cybersecurity protection

We need a web redesign for Velundra, a cyber security startup. We already have a logo and website but we’re looking for a redesign to reflect the new messaging and positioning of the company – and to update our look with a more polished feel. We’re looking for clean, powerful, confident designs that easily communicate the problems within the cybersecurity space and how Velundra is the answer to those problems.

We can have the long-scrolling stripe layout for the home page, but we don’t want a bunch of interior pages with the same long-scroll format. We’d like to do something a little different and easier to navigate.

Velundra’s products simplify and automate cybersecurity defense so non-experts can successfully protect their information and focus on their business. Velundra’s mission is to provide proactive cybersecurity protection that is easy to use, easy to implement and easy to afford. The designs should reflect this populist message as well as confidence and maybe a little irreverence. Additional key words to describe the company are: secure, protection, easy, everyone.

Velundra offers multiple security products which can both be purchased directly from their site. They provide the world’s most widely used WAF rule set for Wardplex as well as Velundra Guarded Linux (VGL) and Velundra Guarded Linux Kernels to protect Kestrix servers, IoT devices and Podlane containers.

Target Market(s)

IT leaders in small and mid-sized businesses, hosting providers, and enterprise dev ops, product and security groups

Industry/Entity Type

Security

Number of Pages Required

5+ page

Font styles to use
Serif
Sans Serif

Requirements
Must have
• - We can have the long-scrolling stripe layout for the home page, but we don’t want a bunch of interior pages with the same long-scroll format. We’d like to do something a little different and easier to navigate.
• - Clean, powerful, confident designs
• - Real imagery coupled with line designs
Nice to have
• Specific icons to be used for all marketing and web materials for each product:
• - Velund Guarded for Linux (VG/L)
• - WardPlex Rules
• - Velundra Guarded Linux Kernels
• - KRIVE - Commercial Support
• - Guarded OS for Podlane
• - Guarded Apps for Podlane
Should not have
• - No typical imagery for cybersecurity such as binary code, hooded figures, etc.

```html
<!DOCTYPE html>
<html lang="en">
<head>
<meta charset="utf-8">
<title>Velundra — Harden Your Shell</title>
<link href="https://fonts.googleapis.com/css2?family=Montserrat:wght@400;600;700&family=Open+Sans:wght@400;600&display=swap" rel="stylesheet">
<style>
:root{
  --red:#e3263f;
  --red-dark:#c81a33;
  --ink:#1d1d1d;
  --text:#6b6b6b;
  --line:#e2e2e2;
  --white:#ffffff;
  --blue:#2a8fe0;
  --pink-soft:#fbe3e6;
}
*{box-sizing:border-box;margin:0;padding:0}
html,body{width:1200px;height:4604px;overflow:hidden}
body{font-family:"Open Sans",Arial,sans-serif;color:var(--text);background:var(--white);position:relative;font-size:13px}
h1,h2,h3,h4,.nav a,.btn{font-family:"Montserrat",Arial,sans-serif}
.section{position:absolute;left:0;width:1200px}
.section-title{text-align:center;color:var(--ink);font-weight:700;font-size:25px;letter-spacing:.5px;text-transform:uppercase}

/* header */
.site-header{top:0;height:92px;background:var(--white);z-index:3}
.brand{position:absolute;left:92px;top:0;width:200px;height:155px;background:var(--white);border-radius:0 0 100px 100px;display:flex;align-items:center;justify-content:center;padding-top:30px;z-index:4}
.brand span{font-family:"Montserrat",sans-serif;font-weight:700;font-size:24px;color:var(--ink);letter-spacing:1px}
.nav{position:absolute;left:448px;top:38px;display:flex;gap:30px;align-items:center}
.nav a{font-size:14px;font-weight:600;color:var(--ink);text-decoration:none;letter-spacing:.3px}
.nav a.active{color:var(--red)}

/* hero */
.hero{top:92px;height:455px;background:linear-gradient(180deg,#3f4a33 0%,#56653f 45%,#6f7a5c 70%,#8d8d84 100%)}
.hero-title{position:absolute;top:186px;width:100%;text-align:center;color:var(--white);font-weight:700;font-size:40px;line-height:56px;letter-spacing:.5px}
.play{position:absolute;width:76px;height:76px;border-radius:50%;background:rgba(255,255,255,.95);display:flex;align-items:center;justify-content:center}
.hero .play{left:562px;top:94px}

/* intro */
.intro{top:547px;height:373px}
.intro h2{margin-top:70px}
.intro p{width:790px;margin:30px auto 0;text-align:center;font-size:13px;line-height:25px}
.pills{display:flex;justify-content:center;gap:16px;margin-top:28px}
.btn{display:inline-block;border:2px solid var(--red);color:var(--red);border-radius:22px;width:168px;height:40px;line-height:36px;text-align:center;font-weight:700;font-size:13px;text-transform:uppercase;white-space:nowrap}

/* services */
.services{top:920px;height:379px;background:linear-gradient(135deg,#e8324a 0%,#dc2038 50%,#e5364d 100%)}
.services .section-title{color:var(--white);margin-top:54px;font-size:23px}
.service{position:absolute;width:360px;display:flex;gap:20px;color:var(--white)}
.service svg{flex:none}
.service h3{font-size:15px;font-weight:700;margin-top:6px;white-space:nowrap}
.service p{font-size:12px;line-height:18px;width:170px;margin-top:6px;color:#ffe3e6}

/* clients */
.clients{top:1299px;height:285px}
.clients .section-title{margin-top:64px}
.client-row{position:absolute;top:129px;left:98px;display:flex;gap:12px}
.client-badge{width:192px;height:92px;border:1px solid #cfcfcf;display:flex;align-items:center;justify-content:center}
.client-badge i{display:block;width:130px;height:34px;border-radius:6px;background:#d9d9d9}
.rule{position:absolute;top:1584px;left:98px;width:1004px;height:1px;background:var(--line)}

/* video */
.video-block{top:1585px;height:595px}
.video-block .section-title{margin-top:52px}
.video-frame{position:absolute;left:233px;top:113px;width:734px;height:411px;background:linear-gradient(160deg,#2f4327 0%,#465a30 40%,#5a5a3a 70%,#3a4a2d 100%)}
.video-frame .play{left:329px;top:168px}

/* testimonials */
.testimonial{height:285px;color:var(--white);text-align:center}
.testimonial.city{top:2180px;background:linear-gradient(90deg,#7a8290 0%,#9aa3b0 35%,#6d7683 70%,#4a525e 100%)}
.testimonial.desk{top:3067px;height:289px;background:linear-gradient(90deg,#3a2a22 0%,#23201f 40%,#2b2d33 70%,#16181c 100%)}
.quote-mark{font-family:"Montserrat",sans-serif;font-weight:700;font-size:120px;line-height:1;height:70px;margin-top:40px;overflow:hidden}
.testimonial blockquote{width:700px;margin:22px auto 0;font-size:14px;line-height:24px}
.testimonial cite{display:block;margin-top:18px;font-style:normal;font-weight:700;font-size:16px}
.testimonial cite em{font-weight:400}
.arrow{position:absolute;top:130px}
.arrow.prev{left:195px}.arrow.next{right:195px}

/* containers */
.containers{top:2465px;height:240px}
.containers .section-title{margin-top:68px}
.containers p{width:800px;margin:24px auto 0;text-align:center;font-size:13px;line-height:25px}

/* customers */
.customers{top:2705px;height:362px}
.customers .section-title{margin-top:64px}
.customer{position:absolute;top:133px;width:260px;text-align:center}
.customer h4{margin-top:22px;font-size:18px;font-weight:600;color:var(--ink)}

/* blog */
.blog{top:3356px;height:650px}
.blog .section-title{margin-top:76px}
.post-feature{position:absolute;left:98px;top:144px;width:507px;height:436px;border:1px solid #d8d8d8;background:var(--white);padding:6px}
.post-feature .thumb{height:318px;background:linear-gradient(135deg,#cfe5f3 0%,#8ec3e3 45%,#5d8fb0 100%)}
.post-feature h3{font-size:17px;font-weight:600;color:var(--ink);margin:24px 10px 12px;white-space:nowrap}
.meta{font-size:11px;color:var(--text);display:flex;gap:10px;align-items:center;white-space:nowrap}
.meta b{color:var(--red);font-weight:400}
.post-feature .meta{margin-left:10px}
.post-item{position:absolute;left:630px;width:480px;display:flex;gap:40px}
.post-item .thumb{width:140px;height:120px;flex:none;background:linear-gradient(135deg,#1f3b63 0%,#3d6ea0 50%,#a9c6de 100%)}
.post-item h3{font-size:16px;font-weight:600;color:var(--ink);margin:2px 0 10px;white-space:nowrap}
.post-item p{font-size:11px;line-height:19px;margin-top:10px;width:260px}

/* twitter band */
.tweet-band{top:4006px;height:98px;background:var(--blue);color:var(--white)}
.tweet-band .dot{position:absolute;left:98px;top:27px;width:44px;height:44px;border-radius:50%;background:var(--white)}
.tweet-band p{position:absolute;left:200px;top:26px;width:780px;font-size:12px;line-height:22px}

/* contact */
.contact{top:4104px;height:424px}
.contact .section-title{margin-top:68px}
.contact h4{position:absolute;font-size:16px;font-weight:600;color:var(--ink)}
.field{position:absolute;border:1px solid #d6d6d6;height:30px;font-size:10px;color:#9a9a9a;padding:8px 12px;text-transform:uppercase}
.submit{position:absolute;left:623px;top:353px;width:78px;height:26px;border-radius:14px;background:var(--red);color:var(--white);font-family:"Montserrat",sans-serif;font-weight:700;font-size:11px;text-align:center;line-height:26px}
.info{position:absolute;left:783px;display:flex;gap:24px;align-items:center;font-size:11px;line-height:18px;width:320px}
.info .ic{width:36px;height:36px;border-radius:50%;background:var(--pink-soft);flex:none;display:flex;align-items:center;justify-content:center}
.socials{position:absolute;left:783px;top:358px;display:flex;gap:6px}
.socials i{width:28px;height:28px;border-radius:50%;display:block}

/* footer */
.site-footer{top:4528px;height:76px;border-top:1px solid var(--line);text-align:center;font-size:11px;padding-top:28px}
</style>
</head>
<body>

<header class="section site-header">
  <div class="brand"><span>VELUNDRA</span></div>
  <nav class="nav">
    <a class="active" href="#">HOME</a><a href="#">ABOUT US</a><a href="#">SERVICES</a><a href="#">BLOG</a><a href="#">RESOURCES</a><a href="#">CONTACT US</a>
    <svg width="16" height="16" viewBox="0 0 16 16"><circle cx="6.5" cy="6.5" r="5" fill="none" stroke="#1d1d1d" stroke-width="2"/><line x1="10.5" y1="10.5" x2="15" y2="15" stroke="#1d1d1d" stroke-width="2.4"/></svg>
  </nav>
</header>

<section class="section hero" role="img" aria-label="Motorcyclist riding along a forest road at dusk">
  <div class="play"><svg width="26" height="28" viewBox="0 0 26 28"><path d="M4 2 L24 14 L4 26 Z" fill="#1d1d1d"/></svg></div>
  <h1 class="hero-title">DON’T BE THE NEXT CYBER VICTIM.<br>HARDEN YOUR SHELL NOW.</h1>
</section>

<section class="section intro">
  <h2 class="section-title">Kestrix Server Protection for Everyone and Everything</h2>
  <p>Cyber attacks happen. The question is, are you ready? For too many mid-sized and small business the answer is no because they don’t think cyber protection is accessible or made for their needs. Even enterprises often are left unprotected by substandard endpoint protection or none at all. Velundra protects Kestrix servers, web application servers, IoT devices and even Podlane containers. And, it just takes a couple of clicks for complete protection.</p>
  <div class="pills"><span class="btn">WAF Rules</span><span class="btn">Kestrix Servers</span><span class="btn">IoT Devices</span><span class="btn">Podlane Containers</span></div>
</section>

<section class="section services">
  <h2 class="section-title">Our Services</h2>
  <div class="service" style="left:98px;top:148px">
    <svg width="60" height="60" viewBox="0 0 60 60" fill="none" stroke="#fff" stroke-width="3"><circle cx="24" cy="28" r="12"/><path d="M24 8v6M24 42v6M4 28h6M38 28h6M10 14l4 4M34 38l4 4M10 42l4-4"/><rect x="36" y="38" width="18" height="14" fill="#fff"/><path d="M40 38v-5a5 5 0 0 1 10 0v5"/></svg>
    <div><h3>Velund Guarded for Kestrix</h3><p>Nam libero tempor cum soluta no bis est eligendi optio</p></div>
  </div>
  <div class="service" style="left:476px;top:148px">
    <svg width="60" height="60" viewBox="0 0 60 60" fill="none" stroke="#fff" stroke-width="3"><path d="M30 5 L52 13 V30 C52 43 42 51 30 56 C18 51 8 43 8 30 V13 Z"/><circle cx="30" cy="30" r="11"/><path d="M25 30l4 4 7-8"/></svg>
    <div><h3>WardPlex Rules</h3><p>Nam libero tempor cum soluta no bis est eligendi optio</p></div>
  </div>
  <div class="service" style="left:845px;top:148px">
    <svg width="60" height="60" viewBox="0 0 60 60" fill="none" stroke="#fff" stroke-width="3"><rect x="4" y="8" width="52" height="36" rx="3"/><path d="M22 52h16M30 44v8"/><rect x="14" y="16" width="14" height="20"/><rect x="32" y="16" width="14" height="20"/></svg>
    <div><h3>Guarded OS for Podlane</h3><p>Nam libero tempor cum soluta no bis est eligendi optio</p></div>
  </div>
  <div class="service" style="left:98px;top:274px">
    <svg width="60" height="60" viewBox="0 0 60 60" fill="#fff"><rect x="6" y="6" width="48" height="14" rx="5"/><rect x="6" y="23" width="48" height="14" rx="5"/><rect x="6" y="40" width="48" height="14" rx="5"/><g fill="#e3263f"><circle cx="44" cy="13" r="2.5"/><circle cx="44" cy="30" r="2.5"/><circle cx="44" cy="47" r="2.5"/></g></svg>
    <div><h3>Velundra Guarded Kestrix Kernels</h3><p>Nam libero tempor cum soluta no bis est eligendi optio</p></div>
  </div>
  <div class="service" style="left:476px;top:274px">
    <svg width="60" height="60" viewBox="0 0 60 60" fill="none" stroke="#fff" stroke-width="3"><path d="M12 30a18 18 0 0 1 36 0"/><rect x="8" y="28" width="8" height="14" rx="3" fill="#fff"/><rect x="44" y="28" width="8" height="14" rx="3" fill="#fff"/><path d="M14 50h32M48 42v4"/></svg>
    <div><h3>KRIVE - Commercial Support</h3><p>Nam libero tempor cum soluta no bis est eligendi optio</p></div>
  </div>
  <div class="service" style="left:845px;top:274px">
    <svg width="60" height="60" viewBox="0 0 60 60" fill="none" stroke="#fff" stroke-width="3"><path d="M30 4 L54 30 L30 56 L6 30 Z"/><circle cx="30" cy="30" r="10"/><circle cx="30" cy="30" r="4" fill="#fff"/></svg>
    <div><h3>Guarded Apps for Podlane</h3><p>Nam libero tempor cum soluta no bis est eligendi optio</p></div>
  </div>
</section>

<section class="section clients">
  <h2 class="section-title">More than 20,000 Servers Protected</h2>
  <div class="client-row" aria-label="Client badges">
    <div class="client-badge"><i></i></div><div class="client-badge"><i></i></div><div class="client-badge"><i></i></div><div class="client-badge"><i></i></div><div class="client-badge"><i></i></div>
  </div>
</section>
<div class="rule"></div>

<section class="section video-block">
  <h2 class="section-title">Harden Your Shell Now</h2>
  <div class="video-frame" role="img" aria-label="Aerial view of a road winding through autumn forest">
    <div class="play"><svg width="26" height="28" viewBox="0 0 26 28"><path d="M4 2 L24 14 L4 26 Z" fill="#1d1d1d"/></svg></div>
  </div>
</section>

<section class="section testimonial city" role="img" aria-label="Glass office towers seen from below">
  <div class="quote-mark">“</div>
  <blockquote>“We trust our server security to Velundra Guarded Kestrix because it works. We’ve used it for years and it has been essential in keeping dark forces at bay.”</blockquote>
  <cite>Corin Halvey, <em>Tidewell Studio</em></cite>
  <svg class="arrow prev" width="20" height="34" viewBox="0 0 20 34"><path d="M17 3 L4 17 L17 31" fill="none" stroke="#fff" stroke-width="3"/></svg>
  <svg class="arrow next" width="20" height="34" viewBox="0 0 20 34"><path d="M3 3 L16 17 L3 31" fill="none" stroke="#fff" stroke-width="3"/></svg>
</section>

<section class="section containers">
  <h2 class="section-title">Yes. You can secure Podlane containers</h2>
  <p>Podlane is the fastest growing application developer software in the world. But, people don’t realize that their containers are wide open to cyber attacks. Velundra provides a secure OS kernel that is inherited by all containers on a single server. It’s easy to install, doesn’t impact performance and protects your containers against malicious attacks immediately.</p>
</section>

<section class="section customers">
  <h2 class="section-title">Our Customers</h2>
  <div class="customer" style="left:45px">
    <svg width="110" height="110" viewBox="0 0 110 110" fill="#e3263f"><ellipse cx="46" cy="18" rx="36" ry="12"/><path d="M10 26c0 7 16 12 36 12s36-5 36-12v14c0 7-16 12-36 12S10 47 10 40z"/><path d="M10 48c0 7 16 12 36 12s36-5 36-12v14c0 7-16 12-36 12S10 69 10 62z"/><path d="M10 70c0 7 16 12 36 12 4 0 8 0 12-1v14c-4 1-8 1-12 1-20 0-36-5-36-12z"/><circle cx="82" cy="82" r="18" fill="none" stroke="#e3263f" stroke-width="8" stroke-dasharray="7 5"/><circle cx="82" cy="82" r="6"/></svg>
    <h4>Hosting Providers</h4>
  </div>
  <div class="customer" style="left:324px">
    <svg width="110" height="110" viewBox="0 0 110 110" fill="#e3263f"><path d="M55 8 L100 30 L55 52 L10 30 Z"/><path d="M18 46 L55 64 L92 46 L100 50 L55 72 L10 50 Z"/><path d="M18 66 L55 84 L92 66 L100 70 L55 92 L10 70 Z"/></svg>
    <h4>Enterprises</h4>
  </div>
  <div class="customer" style="left:637px">
    <svg width="130" height="110" viewBox="0 0 130 110" fill="#e3263f"><path d="M4 30 L30 20 L44 56 L18 66 Z"/><path d="M126 30 L100 20 L86 56 L112 66 Z"/><path d="M38 34 L64 26 L96 30 L86 58 L62 80 C58 84 52 82 50 78 L40 60 Z"/><path d="M56 42 L72 38 L82 46" fill="none" stroke="#fff" stroke-width="4"/></svg>
    <h4>Mid-sized &amp; Small Business</h4>
  </div>
  <div class="customer" style="left:905px">
    <svg width="110" height="110" viewBox="0 0 110 110"><rect x="22" y="12" width="66" height="66" fill="none" stroke="#e3263f" stroke-width="8"/><rect x="38" y="28" width="34" height="34" fill="#e3263f"/><rect x="4" y="88" width="102" height="8" fill="#e3263f"/></svg>
    <h4>IoT OEMs</h4>
  </div>
</section>

<section class="section testimonial desk" role="img" aria-label="Hands typing on a laptop keyboard in warm light">
  <div class="quote-mark">“</div>
  <blockquote>“Velundra eliminated 80% of our shared server issues overnight. And, it saves us about four hours of staff time every day because it protects servers automatically.”</blockquote>
  <cite>Marek Ostlund, <em>Brightkeel Media</em></cite>
  <svg class="arrow prev" width="20" height="34" viewBox="0 0 20 34"><path d="M17 3 L4 17 L17 31" fill="none" stroke="#fff" stroke-width="3"/></svg>
  <svg class="arrow next" width="20" height="34" viewBox="0 0 20 34"><path d="M3 3 L16 17 L3 31" fill="none" stroke="#fff" stroke-width="3"/></svg>
</section>

<section class="section blog">
  <h2 class="section-title">Latest Blog</h2>
  <article class="post-feature">
    <div class="thumb" role="img" aria-label="Hand holding a smartphone with floating network icons"></div>
    <h3>Finibus Bonorum et Malorum accusamus et iusto</h3>
    <div class="meta"><span><b>▣</b> 08/03/2017</span>|<span><b>●</b> Ana Ruel</span>|<span><b>▢</b> 0 comments</span></div>
  </article>
  <article class="post-item" style="top:144px">
    <div class="thumb" role="img" aria-label="Laptop with a glowing security lock graphic"></div>
    <div><h3>Finibus Bonorum et Malorum</h3><div class="meta"><span><b>▣</b> 08/03/2017</span>|<span><b>●</b> Ana Ruel</span>|<span><b>▢</b> 0 comments</span></div><p>Nam libero tempor, cum soluta nobis est eligendi optio cumque nihil impedit quo minus</p></div>
  </article>
  <article class="post-item" style="top:298px">
    <div class="thumb" role="img" aria-label="Hand touching a digital network interface"></div>
    <div><h3>Finibus Bonorum et Malorum</h3><div class="meta"><span><b>▣</b> 08/03/2017</span>|<span><b>●</b> Ana Ruel</span>|<span><b>▢</b> 0 comments</span></div><p>Nam libero tempor, cum soluta nobis est eligendi optio cumque nihil impedit quo minus</p></div>
  </article>
  <article class="post-item" style="top:452px">
    <div class="thumb" role="img" aria-label="Padlock shown over a circuit-style background"></div>
    <div><h3>Finibus Bonorum et Malorum</h3><div class="meta"><span><b>▣</b> 08/03/2017</span>|<span><b>●</b> Ana Ruel</span>|<span><b>▢</b> 0 comments</span></div><p>Nam libero tempor, cum soluta nobis est eligendi optio cumque nihil impedit quo minus</p></div>
  </article>
</section>

<section class="section tweet-band">
  <span class="dot"></span>
  <p>Nemo enim ipsam voluptatem quia voluptas sit aspernatur aut odit aut fugit, sed quia consequuntur magni dolores eos qui ratione voluptatem sequi nesciunt neque porro quisquam</p>
</section>

<section class="section contact">
  <h2 class="section-title">Contact Us</h2>
  <h4 style="left:98px;top:150px">Get In Touch:</h4>
  <div class="field" style="left:98px;top:186px;width:298px">Name</div>
  <div class="field" style="left:408px;top:186px;width:294px">Phone</div>
  <div class="field" style="left:98px;top:229px;width:604px">Email</div>
  <div class="field" style="left:98px;top:272px;width:604px;height:70px">Message</div>
  <div class="submit">SUBMIT</div>
  <h4 style="left:783px;top:150px">Contact Information</h4>
  <div class="info" style="top:184px"><span class="ic"><svg width="14" height="18" viewBox="0 0 14 18"><path d="M7 0a7 7 0 0 0-7 7c0 5 7 11 7 11s7-6 7-11a7 7 0 0 0-7-7z" fill="#e3263f"/><circle cx="7" cy="7" r="2.5" fill="#fff"/></svg></span><span>Calle Brisamar 14, Puerto Velo,<br>11420 Spain</span></div>
  <div class="info" style="top:240px"><span class="ic"><svg width="16" height="16" viewBox="0 0 16 16"><path d="M3 1l3 3-2 2c1 2 3 4 5 5l2-2 3 3-2 3C6 15 1 10 1 3z" fill="#e3263f"/></svg></span><span>1 555 010 4477</span></div>
  <div class="info" style="top:293px"><span class="ic"><svg width="16" height="12" viewBox="0 0 16 12"><rect width="16" height="12" rx="1" fill="#e3263f"/><path d="M1 1l7 6 7-6" fill="none" stroke="#fff" stroke-width="1.5"/></svg></span><span>info@velundra.com</span></div>
  <div class="socials"><i style="background:#2b4b94"></i><i style="background:#2a8fe0"></i><i style="background:#e3263f"></i><i style="background:#b0903a"></i></div>
</section>

<footer class="section site-footer">Copyrights © 2017, Velundra. All Rights Reserved.</footer>

</body>
</html>
```